Business Card Design Project

Double sided business card - logo on one side, my details on the other.

I would like to see two options - my logo on a dark grey/black background and my logo on white.

My details as follows:

Trevin Howsam MBus, MRQT
P: 0471 520 164
E: trevin@trevinhowsam.com
W: www.trevinhowsam.com

Target Market(s)

Managers in business, universities and government.

Industry/Entity Type

Business

Requirements
Must have
• Quorvel, Mintaglo and Brastonet icons

```html
<!DOCTYPE html>
<html lang="en">
<head>
<meta charset="utf-8">
<title>Trevin Howsam – Business Card</title>
<link rel="stylesheet" href="https://fonts.googleapis.com/css2?family=Comfortaa:wght@400&family=Open+Sans:ital,wght@0,400;1,400&display=swap">
<style>
  :root {
    --backdrop: #5a0508;
    --card-dark: #222222;
    --card-light: #3a3a3a;
    --band: #202020;
    --ink: #8c8c8c;
    --ink-soft: #7a7a7a;
    --tile: #4a4a4a;
    --tile-ink: #9a9a9a;
  }
  html, body {
    margin: 0;
    padding: 0;
    width: 1200px;
    height: 786px;
    overflow: hidden;
    background: var(--backdrop);
  }
  .canvas {
    position: relative;
    width: 1200px;
    height: 786px;
    font-family: "Open Sans", Arial, sans-serif;
  }
  .card {
    position: absolute;
    box-shadow: 0 6px 14px rgba(0,0,0,0.45);
    overflow: hidden;
  }
  .card-front {
    left: 290px; top: 52px; width: 594px; height: 338px;
    background: radial-gradient(ellipse at 52% 45%, var(--card-light) 0%, var(--card-dark) 70%);
  }
  .wordmark {
    position: absolute;
    left: 0; right: 0; top: 208px;
    text-align: center;
    font-family: "Comfortaa", "Trebuchet MS", sans-serif;
    font-weight: 400;
    font-size: 38px;
    color: var(--ink);
    letter-spacing: -0.5px;
  }
  .tagline {
    position: absolute;
    left: 158px; top: 262px;
    font-family: "Comfortaa", "Trebuchet MS", sans-serif;
    font-size: 12px;
    color: var(--ink-soft);
  }
  .card-back {
    left: 284px; top: 410px; width: 607px; height: 347px;
    background: radial-gradient(ellipse at 50% 25%, var(--card-light) 0%, var(--card-dark) 70%);
  }
  .details-band {
    position: absolute;
    left: 0; right: 0; top: 105px; height: 138px;
    background: var(--band);
  }
  .holder-name {
    position: absolute;
    left: 158px; top: 123px;
    font-size: 21px;
    color: var(--ink);
  }
  .contact-list {
    position: absolute;
    left: 159px; top: 154px;
    margin: 0;
    display: grid;
    grid-template-columns: 85px auto;
    row-gap: 2px;
    font-size: 16px;
    line-height: 21px;
    color: var(--ink);
  }
  .contact-list dt, .contact-list dd { margin: 0; }
  .contact-list dd { font-style: italic; }
  .social-list {
    position: absolute;
    left: 391px; top: 270px;
    display: flex;
    gap: 10px;
    margin: 0; padding: 0;
    list-style: none;
  }
  .social-item {
    width: 59px; height: 59px;
    background: var(--tile);
    border-radius: 2px;
    display: flex;
    align-items: center;
    justify-content: center;
    font-size: 10px;
    color: var(--tile-ink);
  }
</style>
</head>
<body>
<main class="canvas">
  <section class="card card-front" aria-label="Card front">
    <div class="wordmark">trevinhowsam.com</div>
    <div class="tagline">business advice, research and training</div>
  </section>

  <section class="card card-back" aria-label="Card back">
    <div class="details-band"></div>
    <div class="holder-name">Trevin Howsam MBus, MRQT</div>
    <dl class="contact-list">
      <dt>Phone:</dt><dd>0471 520 164</dd>
      <dt>Fax:</dt><dd>trevin@trevinhowsam.com</dd>
      <dt>Web:</dt><dd>www.trevinhowsam.com</dd>
    </dl>
    <ul class="social-list">
      <li class="social-item">Quorvel</li>
      <li class="social-item">Brastonet</li>
      <li class="social-item">Mintaglo</li>
    </ul>
  </section>
</main>
</body>
</html>
```